Cosmetic retail chain developes private label products. We need package designe for creme soap.

We need package designe for bar creme soap in cardboard package. Benchmark is Tulk. The name of our private label for this product is Nerisa.

```html
<!DOCTYPE html>
<html lang="en">
<head>
<meta charset="utf-8">
<title>Nerisa Creme bar – carton</title>
<link href="https://fonts.googleapis.com/css2?family=Ubuntu:wght@400;500;700&display=swap" rel="stylesheet">
<style>
  :root {
    --stage: #eef0f1;
    --panel-top: #dfe4e5;
    --panel-bottom: #ffffff;
    --brand-blue: #1f4cf2;
    --ink-grey: #6f7275;
    --edge: #d3d8da;
    --wave-fill: #f7f8f8;
    --wave-line: #d6dbdc;
  }
  * { box-sizing: border-box; margin: 0; padding: 0; }
  html, body { width: 1200px; height: 800px; overflow: hidden; }
  body {
    background: var(--stage);
    font-family: "Ubuntu", sans-serif;
    position: relative;
  }
  .panel {
    position: absolute;
    background: linear-gradient(180deg, var(--panel-top) 0%, var(--panel-bottom) 70%);
    border: 1px solid var(--edge);
    overflow: hidden;
  }
  .wave { position: absolute; left: 0; width: 100%; z-index: 1; }

  /* Top face */
  .top-face { left: 40px; top: 50px; width: 500px; height: 330px; }
  .top-face .wave { top: 120px; height: 210px; }
  .brand-name {
    position: absolute; left: 0; right: 0; top: 62px; z-index: 2;
    display: flex; justify-content: center; align-items: center; gap: 12px;
    color: var(--brand-blue); font-weight: 700; font-size: 44px; line-height: 1;
  }
  .brand-name .mark { width: 14px; height: 14px; background: var(--brand-blue); }
  .product-name {
    position: absolute; left: 0; right: 0; top: 212px; z-index: 2;
    text-align: center; color: var(--ink-grey); font-weight: 700; font-size: 28px;
  }
  .claims {
    position: absolute; left: 0; right: 0; top: 262px; z-index: 2;
    text-align: center; color: var(--ink-grey); font-weight: 500; font-size: 17px;
  }
  .claims .dot { display: inline-block; width: 7px; height: 7px; background: var(--brand-blue); margin: 0 6px 2px 14px; }

  /* Bottom face */
  .bottom-face { left: 660px; top: 50px; width: 500px; height: 330px; }
  .bottom-face .wave { top: 175px; height: 155px; }
  .description {
    position: absolute; left: 26px; right: 26px; top: 24px;
    color: var(--brand-blue); font-size: 13.5px; line-height: 1.4;
  }
  .ingredients {
    position: absolute; left: 26px; right: 26px; top: 128px;
    color: var(--brand-blue); font-size: 8.5px; line-height: 1.35;
  }
  .ingredients strong { font-weight: 700; }
  .bottom-brand {
    position: absolute; left: 40px; bottom: 28px; z-index: 2;
    color: var(--brand-blue); font-weight: 700; font-size: 34px;
  }
  .net-weight {
    position: absolute; right: 30px; bottom: 38px; z-index: 2;
    display: flex; align-items: center; gap: 8px;
    color: var(--brand-blue); font-weight: 700; font-size: 16px;
  }

  /* Long sides */
  .side-face { width: 500px; height: 150px; background: linear-gradient(180deg, #ffffff 0%, #e9eced 100%); }
  .front-side { left: 40px; top: 400px; }
  .rear-side { left: 660px; top: 400px; transform: rotate(180deg); }
  .benefits {
    position: absolute; left: 24px; top: 18px; list-style: none;
    color: var(--brand-blue); font-size: 13.5px; line-height: 1.35;
  }
  .benefits li::before { content: "▪ "; }
  .side-brand {
    position: absolute; right: 26px; bottom: 14px;
    color: var(--brand-blue); font-weight: 700; font-size: 34px;
  }

  /* End flaps */
  .end-face { top: 570px; width: 330px; height: 150px; background: linear-gradient(180deg, #ffffff 0%, #e9eced 100%); }
  .end-one { left: 40px; }
  .end-two { left: 660px; }
  .end-label {
    position: absolute; inset: 0;
    display: flex; flex-direction: column; justify-content: center; align-items: center;
    text-align: center;
  }
  .end-label .name { color: var(--brand-blue); font-weight: 700; font-size: 26px; }
  .end-label .sub { color: var(--ink-grey); font-size: 11px; margin-top: 2px; }
</style>
</head>
<body>

  <!-- Top face -->
  <section class="panel top-face">
    <p class="brand-name"><span class="mark"></span>Nerisa</p>
    <svg class="wave" viewBox="0 0 500 210" preserveAspectRatio="none">
      <path d="M0 30 C120 -10 200 95 300 80 C380 68 440 30 500 40 L500 210 L0 210 Z" fill="var(--wave-fill)"/>
      <path d="M0 30 C120 -10 200 95 300 80 C380 68 440 30 500 40" fill="none" stroke="var(--wave-line)" stroke-width="2"/>
    </svg>
    <p class="product-name">Creme bar</p>
    <p class="claims"><span class="dot"></span>Moisturising skin<span class="dot"></span>Gentle cleansing</p>
  </section>

  <!-- Bottom face -->
  <section class="panel bottom-face">
    <p class="description">Cream Bar's mild cleansers help your skin to retain its natural moisture rather than stripping it away. This bar even helps to replenish nutrients that are lost during the cleansing process, where a soap bar can leave your skin feeling tight and rough. Creme Bar leave it feeling softer and healthier-looking.</p>
    <p class="ingredients"><strong>Ingredients:</strong> Sodium Lauroyl Isethionate, Stearic Acid, Sodium Palmitate, Lauric Acid, Aqua, Sodium Isethionate, Sodium Stearate, Cocamidopropyl Betaine, Sodium Palm Kernelate, Glycerin, Parfum, Sodium Chloride, Zinc Oxide, Tetrasodium EDTA, Tetrasodium Etidronate, Alumina, Alpha-Isomethyl Ionone, Benzyl Alcohol, Butylphenyl Methylpropional, Citronellol, Coumarin, Hexyl Cinnamal, Limonene, Linalool.</p>
    <svg class="wave" viewBox="0 0 500 155" preserveAspectRatio="none">
      <path d="M0 45 C90 42 160 10 250 18 C330 25 400 0 500 10 L500 155 L0 155 Z" fill="var(--wave-fill)"/>
      <path d="M0 45 C90 42 160 10 250 18 C330 25 400 0 500 10" fill="none" stroke="var(--wave-line)" stroke-width="2"/>
    </svg>
    <div class="net-weight">
      <span>120g ℮</span>
      <svg width="22" height="22" viewBox="0 0 22 22" aria-label="recycling symbol">
        <circle cx="11" cy="11" r="9" fill="none" stroke="#1f4cf2" stroke-width="2.5" stroke-dasharray="12 3"/>
      </svg>
      <svg width="30" height="22" viewBox="0 0 30 22" aria-label="period after opening symbol">
        <rect x="2" y="6" width="26" height="14" rx="2" fill="none" stroke="#1f4cf2" stroke-width="1.5"/>
        <rect x="4" y="2" width="22" height="5" rx="1.5" fill="none" stroke="#1f4cf2" stroke-width="1.5"/>
      </svg>
    </div>
    <p class="bottom-brand">Nerisa</p>
  </section>

  <!-- Long side, front -->
  <section class="panel side-face front-side">
    <ul class="benefits">
      <li>doesn't dry skin like soap can</li>
      <li>moisturising and mild cleansers help retain skin's moisture</li>
      <li>Leaves skin softer, smoother and healthier-looking</li>
      <li>Suitable for daily use on face, body and hands</li>
      <li>It's not a soap – it's a beauty bar</li>
    </ul>
    <p class="side-brand">Nerisa</p>
  </section>

  <!-- Long side, rear (printed inverted) -->
  <section class="panel side-face rear-side">
    <ul class="benefits">
      <li>doesn't dry skin like soap can</li>
      <li>moisturising and mild cleansers help retain skin's moisture</li>
      <li>Leaves skin softer, smoother and healthier-looking</li>
      <li>Suitable for daily use on face, body and hands</li>
      <li>It's not a soap – it's a beauty bar</li>
    </ul>
    <p class="side-brand">Nerisa</p>
  </section>

  <!-- End flaps -->
  <section class="panel end-face end-one">
    <div class="end-label"><span class="name">Nerisa</span><span class="sub">Creme bar</span></div>
  </section>
  <section class="panel end-face end-two">
    <div class="end-label"><span class="name">Nerisa</span><span class="sub">Creme bar</span></div>
  </section>

</body>
</html>
```